Alder Brookworks highend custom homes

We build Fine lakeside residences and timber builds we specialize in rustic hand made designs along with iron and concrete accents to add a modern touch 90% of my homes are buit on lake front properries attached is my logo and slogan as of now and my previous one

Target Market(s)

High end custom homes

Industry/Entity Type

Custom residential construction

Contact Information for Business Card

Been in buissness 8+ years inssured and reliable

Colors
A7469A
B969AE
D3A5CF
EDDBEB
F8F0F9

Requirements
Must have
• Must have slogan and phone number
Should not have
• A combination of rustic yet modern accents

```html
<!DOCTYPE html>
<html lang="en">
<head>
<meta charset="utf-8">
<title>Alder Brookworks – Business Card</title>
<link rel="stylesheet" href="https://fonts.googleapis.com/css2?family=Anton&family=Poppins:wght@400;500;600;700&display=swap">
<style>
  :root {
    --forest: #4a5a45;
    --orchid: #b969ae;
    --plum: #a7469a;
    --ink: #4d4d4d;
    --paper: #ffffff;
    --backdrop: #ffffff;
  }
  * { box-sizing: border-box; margin: 0; padding: 0; }
  html, body {
    width: 1200px; height: 1200px; overflow: hidden;
    background: var(--backdrop);
    font-family: "Poppins", sans-serif;
  }
  .canvas { position: relative; width: 1200px; height: 1200px; }

  .card {
    position: absolute;
    background: var(--paper);
    box-shadow: 0 4px 14px rgba(0,0,0,0.22);
    overflow: hidden;
  }
  .card--front { left: 250px; top: 145px; width: 706px; height: 413px; }
  .card--back  { left: 250px; top: 648px; width: 704px; height: 410px; }

  .card__art { position: absolute; inset: 0; width: 100%; height: 100%; }

  .brand-panel {
    position: absolute; left: 38px; top: 32px; width: 246px; height: 180px;
    background: var(--paper);
  }
  .brand {
    position: absolute; left: 27px; top: 48px; width: 262px;
    text-align: center; color: var(--forest);
  }
  .brand__mark {
    display: block; width: 100px; height: 100px; margin: 0 auto 24px;
    background: var(--forest);
  }
  .brand__name {
    font-weight: 700; font-size: 23px; line-height: 1.1; letter-spacing: 0.3px;
    text-transform: uppercase; white-space: nowrap;
  }
  .brand__slogan {
    margin-top: 6px; font-weight: 400; font-size: 12.5px; letter-spacing: 0.4px;
    color: var(--ink); text-transform: uppercase; white-space: nowrap;
  }

  .person { position: absolute; right: 46px; top: 36px; text-align: right; }
  .person__name {
    font-family: "Anton", sans-serif; font-size: 39px; line-height: 1;
    letter-spacing: 1.5px; color: var(--forest); text-transform: uppercase;
  }
  .person__role {
    margin-top: 6px; font-family: "Anton", sans-serif; font-size: 20px;
    letter-spacing: 1.2px; color: var(--plum); text-transform: uppercase;
  }

  .phone {
    position: absolute; right: 48px; top: 203px;
    display: flex; align-items: center; gap: 8px;
    font-weight: 600; font-size: 26px; color: var(--forest);
  }
  .icon-box {
    display: inline-flex; align-items: center; justify-content: center;
    background: var(--plum); flex: none;
  }
  .icon-box svg { fill: #fff; }
  .phone .icon-box { width: 24px; height: 24px; }

  .contacts {
    position: absolute; left: 50px; top: 263px; list-style: none;
    font-size: 16.5px; line-height: 22px; color: var(--ink);
  }
  .contacts li { display: flex; align-items: flex-start; gap: 9px; margin-bottom: 2px; }
  .contacts .icon-box { width: 18px; height: 18px; margin-top: 2px; }

  .reg {
    position: absolute; left: 50px; top: 383px; height: 30px;
    display: flex; align-items: center;
    font-weight: 500; font-size: 15px; letter-spacing: 0.5px; color: #fff;
  }

  .back-brand {
    position: absolute; left: 0; right: 0; top: 120px; text-align: center; color: var(--forest);
  }
  .back-brand .brand__mark { width: 104px; height: 104px; margin-bottom: 20px; }
  .back-brand .brand__name { font-size: 25px; }
  .back-brand .brand__slogan { font-size: 13px; }
  .back-line {
    position: absolute; left: 0; right: 0; top: 360px; text-align: center;
    font-family: "Anton", sans-serif; font-size: 15.5px; letter-spacing: 1px;
    color: var(--forest); text-transform: uppercase;
  }
</style>
</head>
<body>
<main class="canvas">

  <section class="card card--front" aria-label="Business card front">
    <svg class="card__art" viewBox="0 0 706 413" aria-hidden="true">
      <polygon points="0,0 310,0 0,209" fill="var(--orchid)"/>
      <line x1="50" y1="249" x2="350" y2="249" stroke="var(--plum)" stroke-width="1.5"/>
      <line x1="358" y1="249" x2="658" y2="249" stroke="var(--orchid)" stroke-width="4"/>
      <polygon points="0,383 460,383 430,413 0,413" fill="var(--forest)"/>
      <polygon points="428,413 560,322 706,365 706,413" fill="var(--plum)"/>
      <circle cx="602" cy="335" r="62" fill="var(--paper)"/>
      <circle cx="602" cy="335" r="56" fill="var(--forest)"/>
      <circle cx="602" cy="335" r="30" fill="var(--orchid)"/>
      <polyline points="588,336 598,346 617,325" fill="none" stroke="var(--paper)" stroke-width="6" stroke-linecap="round" stroke-linejoin="round"/>
    </svg>

    <div class="brand-panel"></div>
    <div class="brand">
      <span class="brand__mark"></span>
      <div class="brand__name">Alder Brookworks</div>
      <div class="brand__slogan">• From lodges to manors •</div>
    </div>

    <div class="person">
      <div class="person__name">Daniel Reyes</div>
      <div class="person__role">Managing Director</div>
    </div>

    <div class="phone">
      <span>+123 4567 8901</span>
      <span class="icon-box">
        <svg width="15" height="15" viewBox="0 0 24 24"><path d="M6.6 10.8a15.1 15.1 0 0 0 6.6 6.6l2.2-2.2a1 1 0 0 1 1-.25 11.4 11.4 0 0 0 3.6.57 1 1 0 0 1 1 1V20a1 1 0 0 1-1 1A17 17 0 0 1 3 4a1 1 0 0 1 1-1h3.5a1 1 0 0 1 1 1c0 1.25.2 2.45.57 3.57a1 1 0 0 1-.25 1z"/></svg>
      </span>
    </div>

    <ul class="contacts">
      <li>
        <span class="icon-box"><svg width="12" height="10" viewBox="0 0 24 18"><path d="M0 0h24v2L12 10 0 2zM0 4.5l12 8 12-8V18H0z"/></svg></span>
        <span>alderbrookworks@email.com</span>
      </li>
      <li>
        <span class="icon-box"><svg width="10" height="13" viewBox="0 0 20 26"><path d="M10 0a10 10 0 0 0-10 10c0 7 10 16 10 16s10-9 10-16A10 10 0 0 0 10 0zm0 14a4 4 0 1 1 0-8 4 4 0 0 1 0 8z"/></svg></span>
        <span>418 Lakeshore Drive<br>Suite 12, Harbor Point<br>MI 49740</span>
      </li>
    </ul>

    <div class="reg">REG NO : 1234567</div>
  </section>

  <section class="card card--back" aria-label="Business card back">
    <div class="back-brand">
      <span class="brand__mark"></span>
      <div class="brand__name">Alder Brookworks</div>
      <div class="brand__slogan">• From lodges to manors •</div>
    </div>
    <div class="back-line">Fine lakeside residences and timber builds</div>
  </section>

</main>
</body>
</html>
```